Marcelo Vantrini
Tenor & Vocal Coach
mvbaritono@quellmail.net
(713) 562-8307
www.voicefromthecore.net
Want two sided postcard / rack card.4" x 9"
Front - vertical - picture in t-shirt, name, title (Tenor & Vocal Coach), contact information
Back - horizontal - picture in jacket, name, title (Tenor & Vocal Coach), contact information, bio (see attachment for words)
Do not leave space for an address.
Looking for an edgy modern design!

Target Market(s)

Young adults

Requirements
Nice to have
• Will pay extra to get a complimentary business card design, two sided

```html
<!DOCTYPE html>
<html lang="en">
<head>
<meta charset="utf-8">
<title>Marcelo Vantrini – Rack Card</title>
<link rel="stylesheet" href="https://fonts.googleapis.com/css2?family=Lato:wght@400;700&display=swap">
<style>
  :root {
    --stage: #c9c6c9;
    --navy: #0d1536;
    --sky: #7fc3d8;
    --sky-light: #a7dbe9;
    --orange: #ec7a22;
    --orange-deep: #e2571e;
    --purple: #6a4a9e;
    --ink: #1d1d26;
    --aqua: #8fdbe6;
    --coral: #f28f8a;
    --white: #ffffff;
  }
  * { margin: 0; padding: 0; box-sizing: border-box; }
  html, body { width: 1200px; height: 799px; overflow: hidden; }
  body {
    background: var(--stage);
    font-family: "Lato", sans-serif;
    position: relative;
  }

  /* Front side – vertical */
  .card-front {
    position: absolute;
    left: 82px; top: 43px;
    width: 312px; height: 701px;
    overflow: hidden;
  }
  .card-front .art { position: absolute; inset: 0; }
  .front-name {
    position: absolute; left: 27px; top: 536px;
    font-weight: 700; font-size: 19px; color: var(--purple);
  }
  .front-title {
    position: absolute; left: 27px; top: 561px;
    font-size: 14px; color: var(--ink);
  }
  .front-contacts {
    position: absolute; left: 27px; top: 623px;
    list-style: none; font-size: 13px; color: var(--ink);
  }
  .front-contacts li { display: flex; align-items: center; gap: 5px; height: 16px; }
  .front-contacts svg { width: 13px; height: 13px; flex: none; }

  /* Back side – horizontal */
  .card-back {
    position: absolute;
    left: 430px; top: 251px;
    width: 698px; height: 311px;
    background: var(--navy);
    overflow: hidden;
    color: var(--white);
  }
  .back-portrait {
    position: absolute; right: 0; top: 17px;
    width: 268px; height: 294px;
    background: radial-gradient(ellipse at 55% 45%, #3b4670 0%, #1f2850 45%, var(--navy) 75%);
  }
  .back-name {
    position: absolute; left: 29px; top: 21px;
    font-weight: 700; font-size: 21px; color: var(--aqua);
  }
  .back-title {
    position: absolute; left: 29px; top: 46px;
    font-size: 15px; color: var(--coral);
  }
  .back-bio {
    position: absolute; left: 29px; top: 80px;
    width: 420px; font-size: 12.4px; line-height: 15.5px;
  }
  .back-bio p { margin-bottom: 15px; }
  .back-bio .cta { color: var(--aqua); text-decoration: underline; margin-bottom: 11px; }
  .back-contacts {
    position: absolute; left: 31px; top: 251px;
    list-style: none; font-size: 12.4px; line-height: 15.7px;
  }
</style>
</head>
<body>

<section class="card-front">
  <svg class="art" viewBox="0 0 312 701" preserveAspectRatio="none">
    <defs>
      <linearGradient id="photoTone" x1="0" y1="0" x2="1" y2="1">
        <stop offset="0" stop-color="#8e8aa8"/>
        <stop offset="0.45" stop-color="#d9d2b0"/>
        <stop offset="1" stop-color="#8c8f99"/>
      </linearGradient>
      <linearGradient id="skyFill" x1="0" y1="0" x2="1" y2="1">
        <stop offset="0" stop-color="var(--sky)"/>
        <stop offset="0.5" stop-color="var(--sky-light)"/>
        <stop offset="1" stop-color="var(--sky)"/>
      </linearGradient>
      <linearGradient id="swoosh" x1="0" y1="0" x2="1" y2="0">
        <stop offset="0" stop-color="var(--orange)"/>
        <stop offset="1" stop-color="var(--orange-deep)"/>
      </linearGradient>
    </defs>
    <rect width="312" height="500" fill="url(#photoTone)" role="img" aria-label="Photo of the singer in a grey t-shirt leaning against a wall"/>
    <path d="M0,349 C60,440 180,470 312,440 L312,485 C180,500 70,460 0,375 Z" fill="url(#swoosh)"/>
    <path d="M0,375 C70,460 180,500 312,485 L312,701 L0,701 Z" fill="url(#skyFill)"/>
    <path d="M0,368 C60,450 140,472 200,502 C260,532 295,570 312,602" fill="none" stroke="var(--white)" stroke-width="1.5"/>
  </svg>

  <h1 class="front-name">Marcelo Vantrini</h1>
  <p class="front-title">Tenor &amp; Vocal Coach</p>
  <ul class="front-contacts">
    <li>
      <svg viewBox="0 0 16 16"><path d="M3.5 1.5l2.6 0.3 1 3-1.6 1.3a9 9 0 0 0 4.4 4.4l1.3-1.6 3 1 .3 2.6-1.8 1.6C7.5 14 2 8.5 1.9 3.3z" fill="var(--purple)"/></svg>
      (713) 562-8307
    </li>
    <li>
      <svg viewBox="0 0 16 16"><rect x="1.5" y="4" width="13" height="9" rx="1" fill="var(--purple)"/><path d="M1.5 4.5l6.5 5 6.5-5" fill="none" stroke="var(--sky-light)" stroke-width="1.2"/></svg>
      mvbaritono@quellmail.net
    </li>
    <li>
      <svg viewBox="0 0 16 16" fill="none" stroke="var(--purple)" stroke-width="1.3"><circle cx="8" cy="8" r="6.5"/><ellipse cx="8" cy="8" rx="3" ry="6.5"/><path d="M1.5 8h13M2.5 4.8h11M2.5 11.2h11"/></svg>
      www.voicefromthecore.net
    </li>
  </ul>
</section>

<section class="card-back">
  <div class="back-portrait" role="img" aria-label="Photo of the singer in a dark blazer and white shirt"></div>
  <h2 class="back-name">Marcelo Vantrini</h2>
  <p class="back-title">Tenor &amp; Vocal Coach</p>
  <div class="back-bio">
    <p>Marcelo is a local singer and actor who has been working professionally around the country as a concert artist and musical theater performer.</p>
    <p>He studied at the Calloway School of Music, Gulfside University and works as a vocal coach with local youths and adults in Houston area.</p>
    <p>Marcelo’s goal is to help his students master their individual instrument so that they can achieve a natural and effortless vocal production.</p>
    <p class="cta">For more information please contact Marcelo today!</p>
  </div>
  <ul class="back-contacts">
    <li>P: (713) 562-8307</li>
    <li>E: mvbaritono@quellmail.net</li>
    <li>W: www.voicefromthecore.net</li>
  </ul>
</section>

</body>
</html>
```